Business Cards/ Stationery for Dental Office
Willow Gate Dental
Business Cards/ Stationery for Dental Office - Health
Creative Brief
Simple
Celia R. Marlow, DDS
2715 Pelton Ridge Franklin, Tn 37069
willowgatedental@mailvane.com
www.willowgatedental.com
Please also add a facebook icon. Link is www.facebook/willowgatedental Also, for the business cards I would like one business card with logo on one side and all pertinent info on the other side. Then another business card (for older people who might actually want an appointment card) that on the back side says Appointment at the top. Then says Name:, Date:, Time:

```html
<!DOCTYPE html>
<html lang="en">
<head>
<meta charset="utf-8">
<title>Willow Gate Dental — Business &amp; Appointment Cards</title>
<link rel="stylesheet" href="https://fonts.googleapis.com/css2?family=Cinzel:wght@500&family=Lato:ital,wght@0,400;0,700;1,400&display=swap">
<style>
  :root{
    --stage:#4b4b4b;
    --card-grey:#8f8f8f;
    --card-white:#ffffff;
    --ink-white:#f4f4f4;
    --accent-gold:#f0c93a;
    --ink-dark:#2b2b2b;
    --rule:#555555;
    --ornament:#a6a6a6;
    --watermark:#efefef;
  }
  *{box-sizing:border-box;margin:0;padding:0}
  html,body{width:1200px;height:761px;overflow:hidden;background:var(--stage)}
  body{position:relative;font-family:"Lato",Arial,sans-serif}

  .card{position:absolute;width:348px;height:240px;border-radius:12px;background:var(--card-grey);overflow:hidden}
  .card--info{left:139px;top:115px}
  .card--logo{left:631px;top:115px}
  .card--stacked{left:139px;top:410px}
  .card--appointment{left:631px;top:410px;background:var(--card-white)}

  .brand{position:absolute;text-align:center}
  .brand__ornament{position:absolute;left:0;right:0;height:9px;border-radius:5px;background:var(--ornament)}
  .brand__dot{width:11px;height:11px;border-radius:50%;background:var(--ink-white);margin:0 auto 6px}
  .brand__name{font-family:"Cinzel",Georgia,serif;font-weight:500;color:var(--ink-white);line-height:1.1;white-space:nowrap}

  .card--info .brand{left:14px;top:62px;width:140px}
  .card--info .brand__ornament.top{top:0}
  .card--info .brand__ornament.bottom{top:112px}
  .card--info .brand__inner{padding-top:18px}
  .card--info .brand__name{font-size:17px}

  .info{position:absolute;left:172px;top:60px;color:var(--ink-white);font-size:8px;line-height:1.5}
  .info__name{color:var(--accent-gold);font-weight:700;font-size:9.5px;margin-bottom:12px}
  .info__address{margin-bottom:9px}
  .contact{display:flex;align-items:center;gap:5px;white-space:nowrap}
  .icon{width:8px;height:8px;flex:none}

  .card--logo .brand{left:80px;top:55px;width:188px}
  .card--logo .brand__ornament.top{top:0}
  .card--logo .brand__ornament.bottom{top:122px}
  .card--logo .brand__inner{padding-top:20px}
  .card--logo .brand__name{font-size:24px}

  .card--stacked .brand{left:92px;top:22px;width:164px}
  .card--stacked .brand__ornament.top{top:0}
  .card--stacked .brand__ornament.bottom{top:106px}
  .card--stacked .brand__inner{padding-top:16px}
  .card--stacked .brand__name{font-size:20px}
  .stacked__name{position:absolute;left:0;right:0;top:150px;text-align:center;color:var(--accent-gold);font-weight:700;font-size:9.5px}
  .stacked__address{position:absolute;left:0;right:0;top:186px;text-align:center;color:var(--ink-white);font-size:7px}
  .stacked__contacts{position:absolute;left:0;right:0;top:200px;display:flex;justify-content:center;flex-wrap:wrap;gap:4px 10px;color:var(--ink-white);font-size:7px;padding:0 24px}

  .appt__watermark{position:absolute;left:110px;right:0;top:102px;text-align:center;font-family:"Cinzel",Georgia,serif;font-weight:500;font-size:26px;line-height:1.1;color:var(--watermark)}
  .appt__title{position:absolute;left:16px;top:28px;font-weight:700;font-size:8.5px;color:var(--ink-dark)}
  .appt__field{position:absolute;left:16px;right:22px;display:flex;align-items:flex-end;gap:5px;font-size:7px;color:var(--ink-dark)}
  .appt__field .line{flex:1;border-bottom:1px solid var(--rule);height:9px}
  .appt__field--day{top:92px}
  .appt__field--time{top:132px}
  .appt__field--with{top:172px}
  .appt__note{position:absolute;left:14px;right:14px;top:214px;text-align:center;font-style:italic;font-size:6.5px;color:var(--ink-dark)}
</style>
</head>
<body>

<section class="card card--info">
  <div class="brand">
    <div class="brand__ornament top" role="img" aria-label="Decorative scroll flourish"></div>
    <div class="brand__inner">
      <div class="brand__dot"></div>
      <div class="brand__name">Willow Gate<br>Dental</div>
    </div>
    <div class="brand__ornament bottom" role="img" aria-label="Decorative scroll flourish"></div>
  </div>
  <div class="info">
    <p class="info__name">Celia R. Marlow, DDS</p>
    <p class="info__address">2715 Pelton Ridge<br>Alder Bend, Tn 38911</p>
    <p class="contact"><svg class="icon" viewBox="0 0 10 10"><path d="M2 1h2l1 2-1.2 1a5 5 0 0 0 2.2 2.2L7 5l2 1v2a1 1 0 0 1-1 1A7 7 0 0 1 1 2a1 1 0 0 1 1-1z" fill="#f4f4f4"/></svg>615-555-0148</p>
    <p class="contact"><svg class="icon" viewBox="0 0 10 10"><rect x="1" y="3" width="8" height="5" fill="#f4f4f4"/><rect x="3" y="1" width="4" height="2" fill="#f4f4f4"/></svg>615-555-0192</p>
    <p class="contact"><svg class="icon" viewBox="0 0 10 10"><rect x="1" y="2" width="8" height="6" fill="#f4f4f4"/><path d="M1 2l4 3 4-3" stroke="#8f8f8f" fill="none"/></svg>willowgatedental@mailvane.com</p>
    <p class="contact"><svg class="icon" viewBox="0 0 10 10"><circle cx="5" cy="5" r="4" fill="none" stroke="#f4f4f4"/><path d="M1 5h8M5 1c-2 2.5-2 5.5 0 8M5 1c2 2.5 2 5.5 0 8" stroke="#f4f4f4" fill="none" stroke-width=".7"/></svg>www.willowgatedental.com</p>
    <p class="contact"><svg class="icon" viewBox="0 0 10 10"><rect x="1" y="1" width="8" height="8" rx="1" fill="#f4f4f4"/></svg>www.facebook/willowgatedental</p>
  </div>
</section>

<section class="card card--logo">
  <div class="brand">
    <div class="brand__ornament top" role="img" aria-label="Decorative scroll flourish"></div>
    <div class="brand__inner">
      <div class="brand__dot"></div>
      <div class="brand__name">Willow Gate<br>Dental</div>
    </div>
    <div class="brand__ornament bottom" role="img" aria-label="Decorative scroll flourish"></div>
  </div>
</section>

<section class="card card--stacked">
  <div class="brand">
    <div class="brand__ornament top" role="img" aria-label="Decorative scroll flourish"></div>
    <div class="brand__inner">
      <div class="brand__dot"></div>
      <div class="brand__name">Willow Gate<br>Dental</div>
    </div>
    <div class="brand__ornament bottom" role="img" aria-label="Decorative scroll flourish"></div>
  </div>
  <p class="stacked__name">Celia R. Marlow, DDS</p>
  <p class="stacked__address">2715 Pelton Ridge Alder Bend, Tn 38911</p>
  <div class="stacked__contacts">
    <span class="contact"><svg class="icon" viewBox="0 0 10 10"><path d="M2 1h2l1 2-1.2 1a5 5 0 0 0 2.2 2.2L7 5l2 1v2a1 1 0 0 1-1 1A7 7 0 0 1 1 2a1 1 0 0 1 1-1z" fill="#f0c93a"/></svg>615-555-0148</span>
    <span class="contact"><svg class="icon" viewBox="0 0 10 10"><rect x="1" y="3" width="8" height="5" fill="#f0c93a"/><rect x="3" y="1" width="4" height="2" fill="#f0c93a"/></svg>615-555-0192</span>
    <span class="contact"><svg class="icon" viewBox="0 0 10 10"><rect x="1" y="2" width="8" height="6" fill="#f0c93a"/><path d="M1 2l4 3 4-3" stroke="#8f8f8f" fill="none"/></svg>willowgatedental@mailvane.com</span>
    <span class="contact"><svg class="icon" viewBox="0 0 10 10"><rect x="1" y="1" width="8" height="8" rx="1" fill="#f0c93a"/></svg>www.facebook/willowgatedental</span>
    <span class="contact"><svg class="icon" viewBox="0 0 10 10"><circle cx="5" cy="5" r="4" fill="none" stroke="#f0c93a"/><path d="M1 5h8M5 1c-2 2.5-2 5.5 0 8M5 1c2 2.5 2 5.5 0 8" stroke="#f0c93a" fill="none" stroke-width=".7"/></svg>www.willowgatedental.com</span>
  </div>
</section>

<section class="card card--appointment">
  <p class="appt__watermark" aria-hidden="true">Willow Gate<br>Dental</p>
  <h2 class="appt__title">Your Next Appointment</h2>
  <div class="appt__field appt__field--day"><span>Appointment Day</span><span class="line"></span></div>
  <div class="appt__field appt__field--time"><span>Appointment Time</span><span class="line"></span><span>a.m.</span><span class="line"></span><span>p.m.</span></div>
  <div class="appt__field appt__field--with"><span>Appointment With</span><span class="line"></span></div>
  <p class="appt__note">We kindly ask for a 24hr notice for cancellation of appointments otherwise a charge may be incurred.</p>
</section>

</body>
</html>
```